■ 依頼の目的/概要
栃木県で左官工事をする会社です。
あたらしく始める事業の宣伝チラシの製作をお願いします。
漆喰を使った壁面のリフォーム事業です。
現在まで大手ゼネコンの下請けとしてやってきましたが建築の業界は未だ先が見えません。そこで自社にて直接ユーザーと仕事をして行きたいと思い今回の事業展開に至ります。

■ デザインへの要望

参考のURLや裏面の記事に関しては用意しましたので添付の資料をご覧下さい。

コンセプト【健康】と【幸せ】をテーマにしております。
表面のデザインは。
寝室・子供部屋・キッチンなどの写真を入れてもらえればと思います。
キャッチコピーは
「健康と幸せを提案する呼吸する壁面」
文言はデザインの都合で若干変更して頂いてかまいません。
日本古来よりある伝統的な技法と地元栃木から作られる原料をアピールしてください。
裏面には記事的な事を入れたいと思っております。
当社にて作成した資料をお使い、また参考程度にしてください。
よろしくお願い致します。

■ 納品ファイルの希望
イラストレーター形式

■ 利用用途

チラシのみ

■ 進め方

弊社の希望するイメージに近い提案を1つ(場合によって複数)選択させて頂きます。希望に近づけるために、修正要望を個別にさせて頂くこともあります。コンペ方式のため、修正後に当選されない場合も、どうかご了承ください。

■ その他/注意点

選択させて頂いたデザインの著作権(財産権)等の扱いはQuorvix利用規約に従い、弊社に譲渡をお願いします。フォントや画像素材などを利用する場合は上記利用用途に使用できることを確認し、第三者の知的財産権等に注意して下さい。
■ 選んだ理由

一般向けのイメージと裏面のレイアウトが決めてでした。

■ 提案者全員へのお礼・コメント

また機会がありましたらよろしくお願いいたします。

```html
<!DOCTYPE html>
<html lang="ja">
<head>
<meta charset="UTF-8">
<title>漆喰リフォーム チラシ 裏面</title>
<link href="https://fonts.googleapis.com/css2?family=Noto+Sans+JP:wght@400;500;700;900&display=swap" rel="stylesheet">
<style>
:root{
  --teal:#2b9fb0;
  --teal-dark:#1f8494;
  --orange:#e27a22;
  --ink:#3a3a3a;
  --plaster:#e9e9e6;
  --paper:#ffffff;
}
*{margin:0;padding:0;box-sizing:border-box}
html,body{width:848px;height:1200px;overflow:hidden;background:var(--paper)}
body{font-family:"Noto Sans JP",sans-serif;color:var(--ink);position:relative}
.intro{position:absolute;left:24px;top:20px;width:800px}
.intro h1{font-size:31px;font-weight:900;color:var(--teal);letter-spacing:1px}
.intro p{margin-top:14px;font-size:12.6px;line-height:1.9;text-align:justify}
.features{position:absolute;left:0;top:254px;width:848px;height:392px;background:var(--plaster)}
.features-title{position:absolute;left:22px;top:16px;display:flex;align-items:center;gap:10px}
.features-title svg{width:40px;height:40px}
.features-title h2{font-size:33px;font-weight:900;color:#505050;letter-spacing:1px}
.feature{position:absolute;width:390px;padding:12px 14px;background:rgba(255,255,255,.55);border-radius:6px}
.feature h3{font-size:17px;font-weight:700;color:var(--orange);margin-bottom:6px;line-height:1.35}
.feature p{font-size:12px;line-height:1.75}
.f1{left:22px;top:74px}.f2{left:436px;top:74px}
.f3{left:22px;top:226px}.f4{left:436px;top:226px}
.consult{position:absolute;left:24px;top:660px;width:800px}
.consult h2{font-size:17px;font-weight:700;color:var(--teal);border:2px solid var(--teal);padding:5px 12px;display:inline-block;background:#f2fafb}
.consult p{margin-top:10px;font-size:12.6px;line-height:1.9;text-align:justify}
.consult .sign{text-align:right;margin-top:4px}
.contact{position:absolute;left:0;top:880px;width:848px;height:320px;background:var(--teal);color:#fff;text-align:center}
.contact .lead{margin-top:20px;font-size:17px;font-weight:500}
.contact .tel{font-size:44px;font-weight:900;letter-spacing:2px;display:flex;justify-content:center;align-items:center;gap:12px;margin-top:2px}
.contact .tel svg{width:38px;height:38px}
.contact .hours{font-size:12px;opacity:.9}
.contact .company{margin-top:18px;font-size:26px;font-weight:700}
.contact .address{font-size:12.5px;margin-top:4px}
</style>
</head>
<body>
<section class="intro">
  <h1>空気ってかなり汚染されているんです。</h1>
  <p>空気の中には、目に見えないウイルスやダニ、カビなどの胞子、ほこりなどがたくさん漂っています。それを呼吸するたびに一緒に吸い込んでいるのです。これは外に限らず、住まいの中でも同じこと。最近はほとんどの住宅で化学物質を含む建材が使われ、シックハウス症候群などの問題もよく耳にするようになりました。24時間、空気清浄機が稼働している家庭も珍しくありませんが、それで本当に十分でしょうか。室内の空気をきれいに保つためには、毎日触れている壁そのものを見直すことが大切です。漆喰は古くから日本の住まいを守ってきた自然素材で、空気中の湿気を吸ったり吐いたりしながら、お部屋を快適な状態に整えてくれます。私たちは地元栃木で採れる原料を使い、伝統の技法で一枚一枚丁寧に仕上げています。家族が長い時間を過ごす寝室や子供部屋、キッチンこそ、呼吸する壁で健康と幸せを守りましょう。</p>
</section>

<section class="features">
  <div class="features-title">
    <svg viewBox="0 0 40 40" aria-hidden="true"><circle cx="20" cy="20" r="18" fill="var(--teal)"/><path d="M12 21l6 6 11-13" stroke="#fff" stroke-width="4" fill="none" stroke-linecap="round" stroke-linejoin="round"/></svg>
    <h2>漆喰の知られざる特徴</h2>
  </div>
  <div class="feature f1">
    <h3>お部屋のジメジメを防ぎます</h3>
    <p>漆喰は、主成分である消石灰が湿気を吸ったり吐いたりする調湿性能を持っています。梅雨の時期は湿気を吸収し、乾燥する冬には水分を放出するため、一年を通して快適な室内環境を保ちます。結露の発生も抑えてくれます。</p>
  </div>
  <div class="feature f2">
    <h3>ペットやたばこの臭いを軽減します</h3>
    <p>ペット専用マンションの增加や室内でペットを飼う家庭が増えています。漆喰は強いアルカリ性で臭いの元となる物質を分解し、ペットやたばこ、生活臭を軽減します。お客様を気持ちよくお迎えできるお部屋になります。</p>
  </div>
  <div class="feature f3">
    <h3>クロス・既存のしっくいからの<br>塗り替えに最適</h3>
    <p>今のクロスを剥がさずに、その上から塗ることができる工法もあります。工期が短く費用も抑えられ、住みながらのリフォームが可能です。古くなった漆喰壁の塗り替えにも対応いたします。</p>
  </div>
  <div class="feature f4">
    <h3>カビの発生を防ぎます</h3>
    <p>漆喰は強いアルカリ性のため、カビや細菌が繁殖しにくい素材です。カビはアレルギーやぜんそくの原因にもなるため、小さなお子様やご高齢の方がいるご家庭に特におすすめです。</p>
  </div>
</section>

<section class="consult">
  <h2>そのための第一歩として「無料相談」をご用意しました。</h2>
  <p>住まいの壁についてのお悩みやご質問に、左官一筋の職人が直接お答えいたします。現在のお部屋の状態を拝見し、ご予算やご希望に合わせた最適なプランをご提案します。お見積りまで費用は一切かかりませんので、どうぞお気軽にお問い合わせください。これまで多くの現場で培ってきた確かな技術で、皆様の健康で幸せな暮らしをお手伝いいたします。地元栃木の素材と職人の手仕事で、心地よい住まいづくりを始めてみませんか。</p>
  <p class="sign">(有)青陽技研　代表　○○</p>
</section>

<footer class="contact">
  <p class="lead">ぜひ一度お電話を</p>
  <p class="tel">
    <svg viewBox="0 0 24 24" aria-hidden="true"><path fill="#fff" d="M6.6 10.8a15.2 15.2 0 006.6 6.6l2.2-2.2a1 1 0 011-.25 11.4 11.4 0 003.6.57 1 1 0 011 1V20a1 1 0 01-1 1A17 17 0 013 4a1 1 0 011-1h3.5a1 1 0 011 1c0 1.25.2 2.45.57 3.57a1 1 0 01-.25 1z"/></svg>
    TEL 028-555-0137
  </p>
  <p class="hours">受付 9:00〜18:00（日曜定休）</p>
  <p class="company">(有)青陽技研</p>
  <p class="address">〒320-0000 栃木県宇都宮市みどり町12-8</p>
</footer>
</body>
</html>
```